Education portal needs a new Email Creative Design

We could not decide on the creative earlier as we were unable to picture how will it look. Hence, we have added content so that we can choose the best design of all. Below is the content to be used for the email creative:
____________________________________
Did you know that 25% of all Americans have experienced at least one divorce?*
41% of first marriages end in divorce!!*

Over 1 million children are affected by divorce each year*

Become a Marriage and Family therapist - Achieve inner-happiness by helping individuals, families and couples resolve their struggles and enhance their lives.
Family Therapists are trained in various modes of therapy in order to prepare them for work with individuals, families, couples, and groups.

With proper training, you will be able to treat:
• Depression and other Affective Disorders
• Childhood Behavioral and Emotional Disorders
• Marital and Relationship Problems
• Conduct Disorder and Delinquency
• Substance Abuse
• Alcoholism
• Domestic Violence
• Severe Mental Illness
• Physical Illness

You could also qualify for financial aid* from the government to pursue this career..

Secure your life by earning upto $78,580* and attain peace of mind while helping others..

__________________________

These are the links to images we liked, but if you have something better, we would love to see them:
http://www.pictovale.example/photo/seperated-50317294?st=7kq2m81
http://www.pictovale.example/photo/domestic-violence-68204937?st=b4n9x52

We are an education portal offering options of schools, colleges, universities and courses to students and working professionals.

We are looking for an email creative which has great call-to-action; be creative and research more if you wish.
Incorporate call-to-action tabs, make it colorful, include pictures and content.
Also attached are industry standard creatives for your reference, let me know if you have any questions.
Updates

Please see new files uploaded

I have uploaded a new creative made by our design team. Follow similar guidelines

For those who have not submitted their designs, please send us soon. Thanks

We thought a content brief will do more justice to this design contest hence we have updated our brief with new content to create a newer design Please submit your designs soon. Thanks

Target Market(s)

25 to 50 years working professionals

Industry/Entity Type

Government

Font styles to use
Serif
Sans Serif
Decorative
Script

Requirements
Must have
• Call-to-action

```html
<!DOCTYPE html>
<html lang="en">
<head>
<meta charset="utf-8">
<title>Marriage and Family Therapist Career Email</title>
<link rel="stylesheet" href="https://fonts.googleapis.com/css2?family=Exo+2:wght@400;500&display=swap">
<style>
  :root {
    --page-bg: #e7e7e9;
    --frame: #9a9a9a;
    --header-bg: #2e0d19;
    --band-maroon: #4b0008;
    --band-peach: #fbd08c;
    --intro-bg: #f6c26f;
    --list-bg: #f2ea9b;
    --closing-bg: #f8e5a5;
    --text-dark: #1c1410;
    --text-light: #ffffff;
    --cta-top: #38c8f4;
    --cta-bottom: #0a72b8;
    --photo-light: #e9eef3;
    --photo-mid: #b9c9da;
  }
  * { box-sizing: border-box; margin: 0; padding: 0; }
  html, body { width: 1000px; height: 1200px; overflow: hidden; }
  body {
    background: var(--page-bg);
    font-family: "Exo 2", "Trebuchet MS", sans-serif;
    color: var(--text-dark);
    position: relative;
  }
  .email {
    position: absolute;
    left: 12px; top: 13px;
    width: 976px; height: 1163px;
    border: 1px solid var(--frame);
    background: var(--closing-bg);
  }
  .header {
    height: 90px;
    background: var(--header-bg);
    color: var(--text-light);
    display: flex; align-items: center; justify-content: center;
    font-size: 47px; font-weight: 400; letter-spacing: 0.5px;
  }
  .hero-photo {
    height: 495px;
    background: linear-gradient(180deg, var(--photo-light) 0%, var(--photo-mid) 100%);
  }
  .cta-band {
    height: 54px;
    background: var(--band-peach);
    border-top: 1px solid #5a2a1a;
    position: relative;
  }
  .cta-button {
    position: absolute;
    left: 286px; top: -48px;
    width: 406px; height: 88px;
    border-radius: 44px;
    background: linear-gradient(180deg, var(--cta-top) 0%, #14a0dc 50%, var(--cta-bottom) 100%);
    border: 2px solid #0a5f99;
    color: var(--text-light);
    display: flex; align-items: center; justify-content: center; gap: 14px;
    font-size: 48px; text-decoration: none;
  }
  .cta-button svg { width: 42px; height: 42px; }
  .headline-band {
    height: 58px;
    background: var(--band-maroon);
    color: var(--text-light);
    display: flex; align-items: center; justify-content: center;
    font-size: 34px; font-weight: 400;
  }
  .intro {
    height: 98px;
    background: var(--intro-bg);
    padding: 9px 30px 0;
    text-align: center;
    font-size: 15.6px; line-height: 20px;
  }
  .benefits {
    height: 231px;
    background: var(--list-bg);
    list-style: none;
    display: grid;
    grid-template-columns: 414px 414px;
    grid-auto-rows: 64px;
    padding: 20px 0 0 82px;
  }
  .benefit { display: flex; align-items: flex-start; gap: 24px; }
  .benefit svg { width: 70px; height: 46px; flex: none; margin-top: 4px; }
  .benefit p { font-size: 18.5px; line-height: 23px; }
  .closing {
    height: 101px;
    border-top: 2px dashed #6a5a3a;
    text-align: center;
    padding-top: 11px;
  }
  .closing .quote { font-size: 15.6px; line-height: 20px; padding: 0 40px; }
  .closing .tagline { font-size: 18.5px; margin-top: 8px; }
  .footer {
    height: 34px;
    background: var(--band-maroon);
    color: var(--text-light);
    display: flex; align-items: center; justify-content: center;
    font-size: 17px;
  }
</style>
</head>
<body>
<svg width="0" height="0" style="position:absolute">
  <defs>
    <symbol id="grad-cap" viewBox="0 0 70 46">
      <rect x="8" y="26" width="52" height="14" rx="7" fill="#f7f1e2" stroke="#b8ad95"/>
      <rect x="38" y="24" width="5" height="18" fill="#c8202a"/>
      <path d="M16 20 L16 30 Q34 38 52 30 L52 20 Z" fill="#1b1b1b"/>
      <path d="M2 14 L34 2 L66 14 L34 26 Z" fill="#262626"/>
      <path d="M34 14 L56 22 L56 32" stroke="#d8a820" stroke-width="2" fill="none"/>
    </symbol>
    <symbol id="chevrons" viewBox="0 0 40 40">
      <path d="M18 6 L6 20 L18 34 M34 6 L22 20 L34 34" stroke="#fff" stroke-width="7" fill="none" stroke-linecap="round" stroke-linejoin="round"/>
    </symbol>
  </defs>
</svg>

<main class="email">
  <header class="header">Area for Website Details</header>

  <div class="hero-photo" role="img" aria-label="Photo of a smiling group of young working professionals in shirts and ties"></div>

  <div class="cta-band">
    <a class="cta-button" href="#">
      <svg><use href="#chevrons"/></svg>
      <span>Click Here</span>
      <svg style="transform:scaleX(-1)"><use href="#chevrons"/></svg>
    </a>
  </div>

  <h1 class="headline-band">Become a Marriage and Family Therapist</h1>

  <p class="intro">Did you know that 25% of all Americans have experienced at least one divorce?* 41% of first marriages end in divorce!!* Over 1 million children are affected by divorce each year.* Achieve inner-happiness by helping individuals, families and couples resolve their struggles and enhance their lives. Family Therapists are trained in various modes of therapy to prepare them for work with individuals, families, couples, and groups.</p>

  <ul class="benefits">
    <li class="benefit"><svg><use href="#grad-cap"/></svg><p>Depression and other<br>Affective Disorders</p></li>
    <li class="benefit"><svg><use href="#grad-cap"/></svg><p>Childhood Behavioral and<br>Emotional Disorders</p></li>
    <li class="benefit"><svg><use href="#grad-cap"/></svg><p>Marital and Relationship<br>Problems</p></li>
    <li class="benefit"><svg><use href="#grad-cap"/></svg><p>Conduct Disorder and<br>Delinquency</p></li>
    <li class="benefit"><svg><use href="#grad-cap"/></svg><p>Substance Abuse and<br>Alcoholism</p></li>
    <li class="benefit"><svg><use href="#grad-cap"/></svg><p>Domestic Violence, Severe Mental<br>and Physical Illness</p></li>
  </ul>

  <section class="closing">
    <p class="quote">With proper training, you will be able to treat all of the conditions above. You could also qualify for financial aid* from the government to pursue this career.</p>
    <p class="tagline">Achieve inner-happiness by helping individuals, families and couples.</p>
  </section>

  <footer class="footer">Secure your life by earning upto $78,580* and attain peace of mind while helping others.</footer>
</main>
</body>
</html>
```